Business Card for Willowcrest Terrain Advisors

We need a business card for Willowcrest Terrain Advisors. The company website address is provided below. The company logo is attached. We provide specialized permafrost services to the mining, transportation, and oil & gas industries. The card should be prepared for:
Dominic Halloway, PhD.
Willowcrest Terrain Advisors
PO Box 418529
Birch Hollow, Alaska 99612
Direct: +1-907-555-2964
Email: dhalloway@terrainadvisors-example.com
Website: www.willowcrestterrainadvisors-example.com

```html
<!DOCTYPE html>
<html lang="en">
<head>
<meta charset="utf-8">
<title>Willowcrest Terrain Advisors – Business Card</title>
<link href="https://fonts.googleapis.com/css2?family=Montserrat:wght@400;500;600&display=swap" rel="stylesheet">
<style>
  :root {
    --backdrop: #9a9a9a;
    --ink: #111820;
    --paper: #ffffff;
    --muted: #5f6368;
  }
  html, body {
    margin: 0;
    padding: 0;
    width: 1149px;
    height: 1200px;
    overflow: hidden;
    background: var(--backdrop);
    font-family: "Montserrat", sans-serif;
  }
  .canvas {
    position: relative;
    width: 1149px;
    height: 1200px;
  }
  .card {
    position: absolute;
    left: 243px;
    width: 663px;
    height: 387px;
    box-sizing: border-box;
  }
  .card--front {
    top: 125px;
    background: var(--ink);
  }
  .card--back {
    top: 630px;
    background: var(--paper);
  }
  .front-wordmark {
    position: absolute;
    left: 0;
    right: 0;
    top: 158px;
    text-align: center;
    color: var(--paper);
    font-weight: 600;
    font-size: 30px;
    letter-spacing: 1px;
  }
  .back-wordmark {
    position: absolute;
    left: 53px;
    top: 52px;
    color: var(--ink);
    font-weight: 600;
    font-size: 19px;
    letter-spacing: 0.5px;
  }
  .name-band {
    position: absolute;
    left: 0;
    top: 133px;
    width: 331px;
    height: 67px;
    background: var(--ink);
    color: var(--paper);
  }
  .name-band .person {
    position: absolute;
    left: 45px;
    top: 9px;
    font-weight: 500;
    font-size: 24px;
    line-height: 1.2;
  }
  .name-band .credential {
    position: absolute;
    left: 45px;
    top: 38px;
    font-weight: 400;
    font-size: 15px;
  }
  .contact-list {
    position: absolute;
    left: 40px;
    top: 254px;
    margin: 0;
    padding: 0;
    list-style: none;
  }
  .contact-list li {
    display: flex;
    align-items: center;
    height: 28px;
    color: var(--muted);
    font-size: 13px;
  }
  .contact-list svg {
    width: 16px;
    height: 16px;
    margin-right: 16px;
    flex: none;
  }
  .address {
    position: absolute;
    left: 459px;
    top: 257px;
    color: var(--muted);
    font-size: 14px;
    line-height: 21px;
  }
</style>
</head>
<body>
<div class="canvas">
  <section class="card card--front">
    <div class="front-wordmark">Willowcrest Terrain Advisors</div>
  </section>

  <section class="card card--back">
    <div class="back-wordmark">Willowcrest Terrain Advisors</div>

    <div class="name-band">
      <div class="person">Dominic Halloway</div>
      <div class="credential">PhD.</div>
    </div>

    <ul class="contact-list">
      <li>
        <svg viewBox="0 0 16 16" aria-hidden="true"><circle cx="8" cy="8" r="8" fill="#111820"/><path d="M5.3 4.5c.4-.3.8-.2 1 .2l.6 1.2c.1.3 0 .6-.2.8l-.4.3c.4.9 1.1 1.6 2 2l.3-.4c.2-.2.5-.3.8-.2l1.2.6c.4.2.5.6.2 1l-.5.6c-.4.4-1 .5-1.6.2-1.8-.8-3.1-2.1-3.9-3.9-.3-.6-.2-1.2.2-1.6z" fill="#fff"/></svg>
        +1-907-555-2964
      </li>
      <li>
        <svg viewBox="0 0 16 16" aria-hidden="true"><circle cx="8" cy="8" r="8" fill="#111820"/><rect x="4.3" y="5.3" width="7.4" height="5.4" rx="0.6" fill="#fff"/><path d="M4.5 5.6 8 8.3l3.5-2.7" fill="none" stroke="#111820" stroke-width="0.8"/></svg>
        dhalloway@terrainadvisors-example.com
      </li>
      <li>
        <svg viewBox="0 0 16 16" aria-hidden="true"><circle cx="8" cy="8" r="8" fill="#111820"/><path d="M6 4.5v6.5l1.6-1.5 1 2.2 1-.5-1-2.1h2.1z" fill="#fff"/></svg>
        www.willowcrestterrainadvisors-example.com
      </li>
    </ul>

    <address class="address" style="font-style:normal">
      PO Box 418529<br>
      Birch Hollow<br>
      Alaska 99612
    </address>
  </section>
</div>
</body>
</html>
```